New Webpage for High Class Expert Witness Services Company

We are looking for a minimalist design for a webpage that just has our logo and an entry form offer to connect with one of our Liaisons.
The entry form should just ask for Name, Email, Contact Info and Description of Project.

Company Name is: The Marlow Crest Advisory Services

Number of Pages Required

1 page

```html
<!DOCTYPE html>
<html lang="en">
<head>
<meta charset="utf-8">
<title>The Marlow Crest Advisory Services – Expert Witness Coordination</title>
<link rel="stylesheet" href="https://fonts.googleapis.com/css2?family=DM+Serif+Display&family=Montserrat:wght@400;500;600&display=swap">
<style>
  :root {
    --bg: #171718;
    --bg-light: #1e1e20;
    --field: #2e2e30;
    --field-border: #48484b;
    --text: #ffffff;
    --muted: #d2d2d4;
    --placeholder: #c4c4c6;
    --icon: #b8b8bb;
    --rule: #3a3a3c;
    --button-top: #ffffff;
    --button-bottom: #dcdcdc;
    --button-text: #1a1a1a;
  }
  * { box-sizing: border-box; margin: 0; padding: 0; }
  html, body { width: 1200px; height: 986px; overflow: hidden; }
  body {
    background: radial-gradient(ellipse at 50% 45%, var(--bg-light) 0%, var(--bg) 70%);
    color: var(--text);
    font-family: "Montserrat", sans-serif;
    position: relative;
  }
  .brand {
    position: absolute; top: 44px; left: 0; width: 1200px;
    display: flex; justify-content: center; align-items: center; gap: 12px;
  }
  .brand-mark { width: 30px; height: 30px; background: #c9c9cb; }
  .brand-name {
    font-family: "Montserrat", sans-serif; font-weight: 500;
    font-size: 22px; letter-spacing: 2px; text-transform: uppercase; color: #d9d9db;
  }
  .heading {
    position: absolute; left: 0; width: 1200px; text-align: center;
    font-family: "DM Serif Display", serif; font-weight: 400;
    font-size: 38px; letter-spacing: 0.5px; line-height: 1;
  }
  .rule {
    position: absolute; left: 547px; width: 107px; height: 2px; background: var(--text);
  }
  .lead {
    position: absolute; top: 269px; left: 0; width: 1200px; text-align: center;
    font-size: 15px; color: var(--muted);
  }
  .field {
    position: absolute; background: var(--field); border: 1px solid var(--field-border);
    border-radius: 6px; display: flex; align-items: flex-start; padding: 15px 14px 0;
    font-size: 12.5px; color: var(--placeholder);
  }
  .field svg { width: 10px; height: 10px; fill: var(--icon); margin: 2px 8px 0 0; flex: none; }
  .field-input { height: 46px; width: 409px; }
  .field-textarea { left: 182px; top: 469px; width: 838px; height: 104px; }
  .submit {
    position: absolute; left: 468px; top: 612px; width: 264px; height: 48px;
    border: none; border-radius: 5px;
    background: linear-gradient(var(--button-top), var(--button-bottom));
    box-shadow: 0 4px 10px rgba(0,0,0,0.55);
    font-family: "Montserrat", sans-serif; font-weight: 600; font-size: 14.5px;
    letter-spacing: 0.6px; color: var(--button-text);
  }
  .about {
    position: absolute; top: 829px; left: 0; width: 1200px; text-align: center;
    font-size: 14px; line-height: 23px; color: var(--text);
  }
  .footer-rule { position: absolute; top: 919px; left: 157px; width: 887px; height: 1px; background: var(--rule); }
  .copyright {
    position: absolute; top: 944px; left: 0; width: 1200px; text-align: center; font-size: 14px;
  }
</style>
</head>
<body>
  <header class="brand">
    <span class="brand-mark"></span>
    <span class="brand-name">The Marlow Crest Advisory Services</span>
  </header>

  <h1 class="heading" style="top:168px">Expert Witness Coordination. Simplified.</h1>
  <div class="rule" style="top:229px"></div>
  <p class="lead">Connect with a dedicated liaison to secure top-tier medical experts tailored to your case.</p>

  <form class="consultation-form">
    <div class="field field-input" style="left:181px;top:330px">
      <svg viewBox="0 0 10 10"><circle cx="5" cy="2.8" r="2.4"/><path d="M0.8 10 Q1 5.6 5 5.6 Q9 5.6 9.2 10Z"/></svg>First Name
    </div>
    <div class="field field-input" style="left:611px;top:330px">
      <svg viewBox="0 0 10 10"><circle cx="5" cy="2.8" r="2.4"/><path d="M0.8 10 Q1 5.6 5 5.6 Q9 5.6 9.2 10Z"/></svg>Last Name
    </div>
    <div class="field field-input" style="left:181px;top:399px">
      <svg viewBox="0 0 10 10"><path d="M0 1.5h10v1.2L5 5.8 0 2.7Z"/><path d="M0 4l5 3 5-3v4.5H0Z"/></svg>Email Address
    </div>
    <div class="field field-input" style="left:611px;top:399px">
      <svg viewBox="0 0 10 10"><path d="M2 0.5l1.8 2.3-1 1.2q1 2 3 3l1.2-1 2.3 1.8-1.3 1.7Q4.5 9 0.5 2Z"/></svg>Phone Number
    </div>
    <div class="field field-textarea">
      <svg viewBox="0 0 10 10"><path d="M7 0.6l2.4 2.4-6 6H1V6.6Z"/><path d="M0.5 9.5l0.5-2.4 1.9 1.9Z"/></svg>Project Description
    </div>
    <button class="submit" type="button">REQUEST CONSULTATION</button>
  </form>

  <h2 class="heading" style="top:735px">The Marlow Crest Advisory Services</h2>
  <div class="rule" style="top:796px"></div>
  <p class="about">Lorem ipsum dolor sit amet, consectetur adipiscing elit, sed do eiusmod tempor incididunt ut labore et dolore magna aliqua.<br>Ut enim ad minim veniam, quis nostrud exercitation ullamco laboris nisi ut aliquip ex ea commodo consequat.</p>

  <div class="footer-rule"></div>
  <footer class="copyright">2026 Copyright ©&nbsp; The Marlow Crest Advisory Services</footer>
</body>
</html>
```